T SHIRT BUSINESS That needs a Flyer of SERVICES offered (LOGO PROVIDED)

I want a flyer created for my Custom Tshirt Design business (SHIRTS IN BLOOM). I want to be able to hand this to a customer so that they can easily find the info they need about my business to be able to contact me for their custom tshirt needs. I would like to display some of our custom artwork that will entice the buyer to SHOP! This flyer should be colorful and bold but please not clutter. I want it to be very professional looking so that when printed on high quality stock it will be attractive.

Target Market(s)

CUSTOM DESIGN CLOTHING AUDIENCE.

Industry/Entity Type

Clothing

Font styles to use
Decorative

Colors
ec1f27
fbed22
0455a3

Requirements
Must have
• Business Info
Name: SHIRTS IN BLOOM
NUMBER: 555-417-3862
email: shirtsinbloom@mailbox.example
website: shirtsinbloom.example
FB: SHIRTSINBLOOM
Instagram: @shirtsinbloom
Business Description: Design Custom Apparel
Type: DTG and Vinyl Printing
SLOGAN: SHIRTS IN BLOOM - WE KEEP IT LOUD!
PRICING: CUSTOM T-SHIRTS STARING @ $25
Nice to have
• Additional inputs from the designer
Should not have
• Please do not make the flyer cluttered.

```html
<!DOCTYPE html>
<html lang="en">
<head>
<meta charset="utf-8">
<title>Shirts In Bloom – Flyer</title>
<link rel="stylesheet" href="https://fonts.googleapis.com/css2?family=Bebas+Neue&family=Arimo:wght@400&display=swap">
<style>
  :root{
    --teal:#0a9fbd;
    --red:#ec1f27;
    --yellow:#fbed22;
    --blue:#0455a3;
    --paper:#ebebeb;
    --white:#ffffff;
    --header-white:#f4f4f4;
  }
  *{box-sizing:border-box;margin:0;padding:0}
  html,body{width:1200px;height:1200px;overflow:hidden}
  body{background:var(--teal);position:relative;font-family:'Arimo',sans-serif}
  .flyer{position:absolute;left:176px;top:52px;width:849px;height:1116px;background:var(--paper);overflow:hidden}
  .backdrop-art{position:absolute;left:22px;top:170px;width:600px;height:680px;
    background:radial-gradient(ellipse at 55% 45%,rgba(214,200,190,.35),rgba(235,235,235,0) 70%)}
  .header{position:absolute;left:0;top:0;width:849px;height:155px}
  .header svg{position:absolute;left:0;top:0}
  .brand-dot{display:block;margin:0 auto 6px;width:40px;height:40px;border:3px solid var(--red);border-radius:50%}
  .brand-wrap{position:absolute;left:48px;top:24px;width:140px;text-align:center}
  .brand-name{font-family:'Bebas Neue',sans-serif;font-size:24px;color:var(--red);letter-spacing:1px;white-space:nowrap}
  .headline{position:absolute;right:32px;top:38px;text-align:right;color:var(--white);font-family:'Bebas Neue',sans-serif;line-height:1}
  .headline .main{font-size:68px;letter-spacing:.5px}
  .headline .sub{font-size:43px;margin-top:3px}
  .slogan{position:absolute;left:59px;top:218px;font-family:'Bebas Neue',sans-serif;font-size:36px;color:var(--blue);white-space:nowrap}
  .badge{position:absolute;left:118px;top:335px}
  .phone{position:absolute;left:53px;top:778px;font-family:'Bebas Neue',sans-serif;font-size:90px;color:var(--red);letter-spacing:1px;line-height:1}
  .contact-panel{position:absolute;left:0;top:875px;width:849px;height:188px;background:var(--white)}
  .contact-list{position:absolute;left:66px;top:887px;list-style:none}
  .contact-list li{display:flex;align-items:center;height:42.5px;font-size:28px;color:var(--blue)}
  .contact-list .icon{width:36px;height:36px;margin-right:22px;flex:none}
  .plain-square{width:34px;height:34px;background:var(--blue);border-radius:3px;margin-right:24px;flex:none}
  .plain-circle{width:34px;height:34px;border:3px solid var(--blue);border-radius:50%;margin-right:24px;flex:none}
  .footer-line{position:absolute;left:0;top:1108px;width:849px;height:8px;background:var(--white)}
  .gallery-item{position:absolute;left:549px;width:264px}
  .g1{top:201px;height:272px;background:linear-gradient(90deg,#5a3a26,#1a1a1a 30%,#1a1a1a 70%,#5a3a26)}
  .g2{top:501px;height:267px;background:linear-gradient(90deg,#1c1c1c 50%,#6a2a22 75%,#3a2a2a)}
  .g3{top:799px;height:264px;background:linear-gradient(90deg,#1c1c1c 50%,#2e3f6a 75%,#3a2a2a)}
</style>
</head>
<body>
  <main class="flyer">
    <div class="backdrop-art" role="img" aria-label="Faint background illustration of a helmeted rider artwork"></div>

    <header class="header">
      <svg width="849" height="155" viewBox="0 0 849 155">
        <rect width="849" height="155" fill="var(--header-white)"/>
        <polygon points="285,0 849,0 849,148 190,148" fill="var(--blue)"/>
        <polygon points="277,0 285,0 190,148 182,148" fill="var(--yellow)"/>
        <polygon points="262,0 277,0 182,148 172,155 176,148" fill="var(--red)"/>
        <polygon points="277,0 287,0 212,115 202,115" fill="var(--yellow)"/>
        <rect x="0" y="148" width="849" height="7" fill="var(--red)"/>
      </svg>
      <div class="brand-wrap">
        <span class="brand-dot"></span>
        <div class="brand-name">SHIRTS IN BLOOM</div>
      </div>
      <div class="headline">
        <div class="main">DESIGN CUSTOM APPAREL</div>
        <div class="sub">DTG AND VINYL PRINTING</div>
      </div>
    </header>

    <p class="slogan">SHIRTS IN BLOOM - WE KEEP IT LOUD!</p>

    <svg class="badge" width="312" height="312" viewBox="0 0 312 312">
      <defs>
        <path id="badge-arc" d="M 50 190 A 112 112 0 1 1 270 190"/>
      </defs>
      <circle cx="156" cy="156" r="153" fill="none" stroke="var(--red)" stroke-width="2.5"/>
      <circle cx="156" cy="156" r="102" fill="none" stroke="var(--red)" stroke-width="2.5"/>
      <text font-family="Bebas Neue, sans-serif" font-size="42" fill="var(--blue)">
        <textPath href="#badge-arc" startOffset="50%" text-anchor="middle">CUSTOM T-SHIRTS STARTING @</textPath>
      </text>
      <text x="153" y="196" text-anchor="middle" font-family="Bebas Neue, sans-serif" font-size="128" fill="var(--blue)">$25</text>
      <g fill="var(--blue)" font-size="22" text-anchor="middle" font-family="Arimo, sans-serif">
        <text x="60" y="248">★</text>
        <text x="252" y="248">★</text>
        <text x="100" y="276">★</text>
        <text x="214" y="276">★</text>
        <text x="156" y="296" font-size="36">★</text>
      </g>
    </svg>

    <div class="phone">555 417 3862</div>

    <div class="contact-panel"></div>
    <ul class="contact-list">
      <li>
        <svg class="icon" viewBox="0 0 36 36" fill="none" stroke="var(--blue)" stroke-width="2.5">
          <rect x="2" y="7" width="32" height="22" rx="2"/>
          <path d="M2 8 L18 21 L34 8 M2 28 L13 17 M34 28 L23 17"/>
        </svg>
        shirtsinbloom@mailbox.example
      </li>
      <li>
        <svg class="icon" viewBox="0 0 36 36" fill="none" stroke="var(--blue)" stroke-width="2.5">
          <circle cx="18" cy="18" r="16"/>
          <ellipse cx="18" cy="18" rx="7" ry="16"/>
          <path d="M2 18 H34 M5 10 H31 M5 26 H31 M18 2 V34"/>
        </svg>
        shirtsinbloom.example
      </li>
      <li><span class="plain-square"></span>SHIRTSINBLOOM</li>
      <li><span class="plain-circle"></span>@shirtsinbloom</li>
    </ul>

    <div class="gallery-item g1" role="img" aria-label="Black t-shirt with orange snake and hand graphic on a wooden backdrop"></div>
    <div class="gallery-item g2" role="img" aria-label="Black t-shirt on a hanger with flaming helmet rider graphic beside a large print of the artwork"></div>
    <div class="gallery-item g3" role="img" aria-label="Black t-shirt on a hanger with motorcycle rider graphic beside a large print of the artwork"></div>

    <div class="footer-line"></div>
  </main>
</body>
</html>
```